Varemo Group Business Card Design

The CEO is looking for a new trendy look for his business card.
You can stay with current branding or come up with something new/creative. It can be 3D, including Medical Office buildings. You can use our logo in a variety of colors. Please include name, title, company name, company website, email address, cell number

Target Market(s)

Real Estate Development and Construction

Industry/Entity Type

Health care real estate

Contact Information for Business Card

Rohesh Kumbar, CEO M-727.418.9062 E-roheshkumbar@varemo.com Address:4100 Lindell Ave, Tampa, FL 33611 www.varemo.com

Font styles to use
Other font styles liked:
• Be creative

Requirements
Must have
• Creative, trendy look
Nice to have
• Please go to our website to get a feel- www. varemo.com
Should not have
• small fonts

```html
<!DOCTYPE html>
<html lang="en">
<head>
<meta charset="utf-8">
<title>Varemo Group Business Card Design</title>
<link rel="stylesheet" href="https://fonts.googleapis.com/css2?family=Archivo:wght@500;600;800&family=Arimo:wght@400&display=swap">
<style>
  :root {
    --sheet: #d9dadc;
    --ink: #1a1718;
    --paper: #ffffff;
    --snow: #f4f4f4;
    --mist: #e8e9e9;
    --crimson: #b01f2a;
    --navy: #1f2d4f;
  }
  * { box-sizing: border-box; margin: 0; padding: 0; }
  html, body { width: 1050px; height: 1200px; overflow: hidden; }
  body {
    background: var(--sheet);
    position: relative;
    font-family: "Archivo", "Arial", sans-serif;
    color: var(--ink);
  }
  .side-label {
    position: absolute;
    top: 52px;
    width: 200px;
    margin-left: -100px;
    text-align: center;
    font-family: "Arimo", "Arial", sans-serif;
    font-weight: 400;
    font-size: 42px;
    letter-spacing: 1px;
    color: var(--ink);
  }
  .card {
    position: absolute;
    overflow: hidden;
  }
  .card--wide { width: 450px; height: 259px; }
  .card--tall { width: 261px; height: 449px; }

  .backdrop {
    position: absolute;
    inset: 0;
  }
  .backdrop--mono {
    background:
      linear-gradient(90deg, transparent 0%, transparent 62%, var(--ink) 62%, var(--ink) 100%),
      linear-gradient(180deg, var(--ink) 0%, var(--ink) 66%, var(--snow) 66%, var(--snow) 100%);
  }
  .backdrop--crimson {
    background: linear-gradient(90deg, var(--crimson) 0%, var(--crimson) 20%, var(--ink) 20%, var(--ink) 30%, var(--crimson) 30%, #8e1822 100%);
  }
  .backdrop--tall {
    background: linear-gradient(180deg, var(--snow) 0%, var(--snow) 45%, var(--ink) 45%, var(--ink) 100%);
  }
  .backdrop--faint {
    background: radial-gradient(ellipse at 40% 40%, var(--mist) 0%, var(--mist) 45%, var(--paper) 75%);
  }

  .wordmark {
    position: absolute;
    font-family: "Archivo", "Arial", sans-serif;
    font-weight: 800;
    line-height: 1;
    letter-spacing: -0.5px;
    white-space: nowrap;
  }
  .wordmark--light { color: var(--paper); }
  .wordmark--dark { color: var(--ink); }
  .wordmark--red { color: var(--crimson); }

  .holder-name {
    position: absolute;
    font-weight: 800;
    font-size: 17px;
    letter-spacing: 0.3px;
  }
  .holder-title {
    position: absolute;
    font-weight: 800;
    font-size: 13px;
    letter-spacing: 0.6px;
  }
  .contact-lines, .address-lines {
    position: absolute;
    list-style: none;
    font-weight: 600;
    font-size: 13.5px;
    line-height: 16px;
  }
  .address-lines { text-align: right; }
  .contact-lines .key {
    display: inline-block;
    width: 20px;
    font-weight: 500;
  }
  .divider {
    position: absolute;
    width: 30px;
    height: 4px;
    background: var(--ink);
  }
  .accent .holder-name, .accent .key { color: var(--crimson); }
  .accent .holder-title, .accent .contact-lines, .accent .address-lines { color: var(--navy); }
</style>
</head>
<body>
  <div class="side-label" style="left:288px">BACK</div>
  <div class="side-label" style="left:764px">FACE</div>

  <!-- Row 1 -->
  <section class="card card--wide" style="left:63px; top:119px">
    <div class="backdrop backdrop--mono" role="img" aria-label="Large black and white monogram letter decoration"></div>
    <div class="wordmark wordmark--light" style="left:110px; top:110px; font-size:26px">Varemo Group</div>
  </section>

  <section class="card card--wide" style="left:538px; top:119px; background:var(--paper)">
    <div class="backdrop backdrop--faint" role="img" aria-label="Faint large monogram letter decoration"></div>
    <div class="holder-name" style="left:30px; top:42px">Rohesh Kumbar</div>
    <div class="holder-title" style="left:30px; top:64px">CEO</div>
    <div class="wordmark wordmark--dark" style="right:36px; top:46px; font-size:22px">Varemo Group</div>
    <ul class="contact-lines" style="left:30px; top:196px">
      <li><span class="key">M</span>727 418 9062</li>
      <li><span class="key">E</span>roheshkumbar@varemo.com</li>
      <li><span class="key">W</span>www.varemo.com</li>
    </ul>
    <ul class="address-lines" style="right:36px; top:196px">
      <li>4100 Lindell Ave</li>
      <li>Tampa, FL</li>
      <li>33611</li>
    </ul>
  </section>

  <!-- Row 2 -->
  <section class="card card--wide" style="left:63px; top:403px">
    <div class="backdrop backdrop--crimson" role="img" aria-label="Large red company name letters on black"></div>
    <div class="wordmark wordmark--light" style="left:132px; top:116px; font-size:34px">Varemo Group</div>
  </section>

  <section class="card card--wide accent" style="left:538px; top:403px; background:var(--paper)">
    <div class="backdrop backdrop--faint" role="img" aria-label="Faint large monogram letter decoration"></div>
    <div class="holder-name" style="left:30px; top:42px">Rohesh Kumbar</div>
    <div class="holder-title" style="left:30px; top:64px">CEO</div>
    <div class="wordmark wordmark--red" style="right:36px; top:46px; font-size:22px">Varemo Group</div>
    <ul class="contact-lines" style="left:30px; top:196px">
      <li><span class="key">M</span>727 418 9062</li>
      <li><span class="key">E</span>roheshkumbar@varemo.com</li>
      <li><span class="key">W</span>www.varemo.com</li>
    </ul>
    <ul class="address-lines" style="right:36px; top:196px">
      <li>4100 Lindell Ave</li>
      <li>Tampa, FL</li>
      <li>33611</li>
    </ul>
  </section>

  <!-- Row 3 -->
  <section class="card card--tall" style="left:252px; top:689px">
    <div class="backdrop backdrop--tall" role="img" aria-label="Large white monogram letter decoration on black"></div>
    <div class="wordmark wordmark--light" style="left:29px; top:383px; font-size:22px">Varemo Group</div>
  </section>

  <section class="card card--tall" style="left:538px; top:689px; background:var(--paper)">
    <div class="backdrop backdrop--faint" role="img" aria-label="Faint large monogram letter decoration"></div>
    <div class="wordmark wordmark--dark" style="left:32px; top:42px; font-size:22px">Varemo Group</div>
    <div class="holder-name" style="left:32px; top:237px">Rohesh Kumbar</div>
    <div class="holder-title" style="left:32px; top:258px">CEO</div>
    <div class="divider" style="left:32px; top:286px"></div>
    <ul class="contact-lines" style="left:32px; top:312px">
      <li><span class="key">M</span>727 418 9062</li>
      <li><span class="key">E</span>roheshkumbar@varemo.com</li>
      <li><span class="key">W</span>www.varemo.com</li>
    </ul>
    <ul class="contact-lines" style="left:32px; top:374px">
      <li>4100 Lindell Ave</li>
      <li>Tampa, FL</li>
      <li>33611</li>
    </ul>
  </section>
</body>
</html>
```